Website Design for Professional Services Company

• Create a new website design that is easy to maintain inside of WordPress with a main page design, a design for generic content pages, and a design for customer case studies. Our current design relies on a number of plugins to function, and we would like to get away from that as much as possible. Our current design also requires a fair amount of coding that we would like to get away from. The more we can use native WordPress the better. We are not opposed to a small subset of plugins that are widely used and readily updated. Our current website can be found at https://tarnwickconsulting.com/. Our fonts (for use in graphics, we don’t want custom fonts on the website itself to make sure it always displays correctly) and colors are as follows:
o Tarnwick Blue:
 #1b75bc
o Tarnwick Grey:
 #6d6f71
o Main Font:
 Telegrafico
o Accent Font:
 Nexa Light

```html
<!DOCTYPE html>
<html lang="en">
<head>
<meta charset="utf-8">
<title>Tarnwick Consulting</title>
<link href="https://fonts.googleapis.com/css2?family=Michroma&family=Montserrat:wght@400;500;600;700&display=swap" rel="stylesheet">
<style>
:root{
  --tarnwick-blue:#1b75bc;
  --tarnwick-blue-dark:#135a93;
  --tarnwick-grey:#6d6f71;
  --ink:#1f2328;
  --soft:#f3f6f9;
  --white:#ffffff;
  --line:#dfe4ea;
}
*{box-sizing:border-box;margin:0;padding:0}
html,body{width:1200px;height:4664px;overflow:hidden}
body{position:relative;background:var(--white);font-family:"Montserrat",Arial,sans-serif;color:var(--tarnwick-grey);font-size:14px;line-height:1.6}
.display{font-family:"Michroma","Montserrat",sans-serif;letter-spacing:.04em}
section,header,footer{position:absolute;left:0;width:1200px}

/* header */
.site-header{top:0;height:140px;background:var(--white)}
.brand{position:absolute;display:flex;align-items:center;gap:12px}
.brand-square{width:34px;height:34px;background:var(--tarnwick-blue)}
.brand-name{font-family:"Michroma",sans-serif;font-size:26px;color:var(--tarnwick-blue);letter-spacing:.08em}
.site-header .brand{left:40px;top:48px}
.contact-strip{position:absolute;right:40px;top:22px;display:flex;gap:30px;font-size:12px;font-weight:600;color:var(--ink)}
.contact-strip span{display:flex;align-items:center;gap:8px}
.contact-strip i{width:24px;height:24px;border-radius:50%;background:var(--tarnwick-blue);display:inline-flex;align-items:center;justify-content:center}
.main-nav{position:absolute;right:40px;top:80px;display:flex;gap:34px;font-size:12px;font-weight:600;color:var(--ink);letter-spacing:.06em}
.main-nav a{color:inherit;text-decoration:none;padding-bottom:8px}
.main-nav a.active{color:var(--tarnwick-blue);border-bottom:2px solid var(--tarnwick-blue)}

/* hero */
.hero{top:140px;height:780px;background:linear-gradient(110deg,#e9eef4 0%,#8ea4bd 38%,#2f5f93 70%,#1d4e82 100%)}
.hero-hex{position:absolute;left:630px;top:90px;width:540px;height:520px}
.hero-copy{position:absolute;left:670px;top:210px;width:460px;text-align:center;color:var(--white)}
.hero-copy .kicker{font-size:24px}
.hero-copy h1{font-size:32px;line-height:1.25;font-weight:400;white-space:nowrap}
.hero-copy .sub{font-size:16px;margin-top:4px}
.hero-copy p{font-size:13px;margin:18px auto 0;width:360px;line-height:1.55}
.btn{display:inline-block;font-size:11px;font-weight:700;letter-spacing:.08em;padding:11px 24px;border-radius:22px;text-decoration:none}
.btn-light{background:var(--white);color:var(--tarnwick-blue);margin-top:26px}
.btn-blue{background:var(--tarnwick-blue);color:var(--white)}

/* section headings */
.section-title{text-align:center;color:var(--tarnwick-blue);font-weight:400}
.eyebrow{text-align:center;font-size:13px;font-weight:700;color:var(--ink)}

/* values */
.values{top:960px;height:380px}
.values .section-title{font-size:26px;margin-top:48px}
.value-row{position:absolute;top:120px;left:70px;display:flex;gap:30px}
.value-card{width:247px;height:200px;background:var(--white);box-shadow:0 4px 18px rgba(0,0,0,.12);text-align:center;padding:28px 22px}
.icon-badge{width:54px;height:54px;border-radius:12px;background:var(--tarnwick-blue);margin:0 auto 14px;display:flex;align-items:center;justify-content:center}
.value-card h3{font-size:13px;font-weight:700;color:var(--ink);letter-spacing:.06em}
.value-card p{font-size:12px;line-height:1.5;margin-top:6px}

/* about */
.about{top:1340px;height:760px}
.about-media{position:absolute;left:130px;top:40px;width:440px;height:660px;background:linear-gradient(160deg,#c9d3de,#4f6781 55%,#26384d)}
.about-copy{position:absolute;left:680px;top:170px;width:400px}
.about-copy .small{font-size:14px;font-weight:700;color:var(--ink)}
.about-copy h2{font-size:40px;color:var(--tarnwick-blue);font-weight:400;padding-bottom:10px;border-bottom:2px solid var(--tarnwick-blue);display:inline-block}
.about-copy p{font-size:13px;margin-top:22px}
.about-copy h4{font-size:13px;color:var(--tarnwick-blue);margin-top:26px;letter-spacing:.06em}
.about-copy h4+p{margin-top:8px}
.about-copy .btn{margin-top:30px}

/* services */
.services{top:2140px;height:560px}
.services .eyebrow{margin-top:28px}
.services .section-title{font-size:40px;margin-top:6px}
.service-row{position:absolute;top:160px;left:70px;display:flex;gap:30px}
.service-card{width:247px;height:400px;background:var(--white);box-shadow:0 4px 18px rgba(0,0,0,.12);text-align:center}
.service-card.featured{outline:3px solid var(--tarnwick-blue)}
.service-media{height:175px}
.service-card h3{font-size:12px;font-weight:700;color:var(--tarnwick-blue);margin:26px 14px 10px;letter-spacing:.06em}
.service-card p{font-size:12px;line-height:1.55;margin:0 22px}

/* why */
.why{top:2720px;height:780px}
.why .eyebrow{margin-top:36px}
.why .section-title{font-size:40px;margin-top:6px;color:var(--ink)}
.why-rule{width:60px;height:3px;background:var(--tarnwick-blue);margin:10px auto 0}
.why .intro{width:880px;margin:26px auto 0;text-align:center;font-size:13px;color:var(--ink)}
.why-media{position:absolute;left:455px;top:290px;width:290px;height:370px;background:linear-gradient(180deg,#dfe7ef,#7f97b2 50%,#2d5b8c)}
.pillar{position:absolute;display:flex;align-items:center;gap:14px;font-weight:700;font-size:14px;color:var(--ink);letter-spacing:.08em}
.pillar .icon-badge{margin:0;width:50px;height:50px;border-radius:50%}

/* blog */
.blog{top:3500px;height:660px}
.blog .small{position:absolute;left:90px;top:20px;font-size:13px;font-weight:700;color:var(--ink)}
.blog h2{position:absolute;left:90px;top:42px;font-size:40px;color:var(--tarnwick-blue);font-weight:400}
.blog-arrows{position:absolute;right:90px;top:48px;display:flex;gap:14px}
.blog-arrows span{width:56px;height:56px;border-radius:50%;display:flex;align-items:center;justify-content:center}
.blog-row{position:absolute;top:140px;left:90px;display:flex;gap:45px}
.post-card{width:310px;height:470px;background:var(--white);box-shadow:0 4px 18px rgba(0,0,0,.12);padding:14px}
.post-card.featured{outline:2px solid var(--tarnwick-blue)}
.post-media{height:240px}
.post-date{display:flex;align-items:center;gap:8px;font-size:11px;color:var(--ink);margin-top:18px}
.post-card h3{font-size:13px;color:var(--ink);font-weight:700;margin-top:10px;letter-spacing:.04em}
.post-card p{font-size:12px;line-height:1.5;margin-top:6px}
.post-card .btn{margin-top:16px;padding:9px 22px}

/* footer */
.site-footer{top:4160px;height:504px;background:var(--tarnwick-blue);color:var(--white)}
.site-footer .brand{left:120px;top:120px;flex-direction:column}
.site-footer .brand-square{background:var(--white);width:60px;height:60px}
.site-footer .brand-name{color:var(--white);font-size:30px}
.socials{position:absolute;left:150px;top:250px;display:flex;gap:12px}
.socials span{width:34px;height:34px;border-radius:50%;border:2px solid var(--white)}
.foot-col{position:absolute;top:100px;font-size:12px}
.foot-col h4{font-size:12px;letter-spacing:.08em;margin-bottom:16px;border-bottom:2px solid var(--white);display:inline-block;padding-bottom:4px}
.foot-col li{list-style:none;margin-bottom:8px;display:flex;gap:10px;align-items:center}
.foot-col li::before{content:"";width:6px;height:6px;flex:none;background:var(--white);border-radius:50%}
.subscribe{display:flex;margin-top:16px}
.subscribe span{flex:1;height:40px;background:var(--white);color:var(--tarnwick-grey);font-size:11px;padding:11px 12px}
.subscribe b{width:46px;height:40px;background:var(--tarnwick-blue-dark);display:flex;align-items:center;justify-content:center}
.copyright{position:absolute;left:0;bottom:0;width:1200px;height:44px;border-top:1px solid rgba(255,255,255,.3);text-align:center;font-size:11px;line-height:44px}
</style>
</head>
<body>

<header class="site-header">
  <div class="brand"><span class="brand-square"></span><span class="brand-name">TARNWICK</span></div>
  <div class="contact-strip">
    <span><i><svg width="12" height="12" viewBox="0 0 24 24"><path fill="#fff" d="M6.6 10.8a15 15 0 006.6 6.6l2.2-2.2a1 1 0 011-.25 11.4 11.4 0 003.6.57 1 1 0 011 1V20a1 1 0 01-1 1A17 17 0 013 4a1 1 0 011-1h3.5a1 1 0 011 1c0 1.250.2 2.45.57 3.6a1 1 0 01-.25 1z"/></svg></i>(555) 014-2290</span>
    <span><i><svg width="12" height="12" viewBox="0 0 24 24"><path fill="#fff" d="M3 5h18v14H3z"/><path fill="none" stroke="#1b75bc" stroke-width="2" d="M3 6l9 7 9-7"/></svg></i>info@tarnwickconsulting.com</span>
  </div>
  <nav class="main-nav"><a class="active" href="#">HOME</a><a href="#">ABOUT US</a><a href="#">SERVICES</a><a href="#">BLOG</a><a href="#">CONTACT US</a></nav>
</header>

<section class="hero" role="img" aria-label="Consultant in a suit working on a tablet with glowing finance chart overlays">
  <svg class="hero-hex" viewBox="0 0 540 520" aria-hidden="true"><polygon points="270,0 540,130 540,390 270,520 0,390 0,130" fill="#1b75bc" fill-opacity=".9"/></svg>
  <div class="hero-copy">
    <div class="kicker display">INNOVATIVE</div>
    <h1 class="display">EPM SOLUTIONS</h1>
    <div class="sub display">FOR FINANCE AND BEYOND</div>
    <p>Tarnwick Consulting provides decades of experience implementing Meridian EPM products with unique and innovative solutions to challenging business processes not only in Finance and Accounting but across organizations.</p>
    <a class="btn btn-light" href="#">DISCOVER MORE</a>
  </div>
</section>

<section class="values">
  <h2 class="section-title display">OUR CORE VALUES PROVIDE OUR FOUNDATION</h2>
  <div class="value-row">
    <div class="value-card"><div class="icon-badge"><svg width="26" height="26" viewBox="0 0 24 24"><circle cx="12" cy="8" r="4" fill="#fff"/><path d="M4 21a8 8 0 0116 0z" fill="#fff"/></svg></div><h3>CLIENTS FIRST</h3><p>Always do the right thing for the client, no exceptions.</p></div>
    <div class="value-card"><div class="icon-badge"><svg width="26" height="26" viewBox="0 0 24 24"><path d="M5 12l5 5 9-10" fill="none" stroke="#fff" stroke-width="3"/></svg></div><h3>INTEGRITY</h3><p>Have integrity and be honest with the client and each other.</p></div>
    <div class="value-card"><div class="icon-badge"><svg width="26" height="26" viewBox="0 0 24 24"><circle cx="12" cy="10" r="6" fill="#fff"/><rect x="9" y="17" width="6" height="4" fill="#fff"/></svg></div><h3>INNOVATION</h3><p>Never satisfied with product limitations, we always find a way.</p></div>
    <div class="value-card"><div class="icon-badge"><svg width="26" height="26" viewBox="0 0 24 24"><circle cx="8" cy="8" r="3" fill="#fff"/><circle cx="16" cy="8" r="3" fill="#fff"/><path d="M2 19a6 6 0 0112 0zM10 19a6 6 0 0112 0z" fill="#fff"/></svg></div><h3>TEAMWORK</h3><p>Clients get all of our together, not just one of us.</p></div>
  </div>
</section>

<section class="about">
  <div class="about-media" role="img" aria-label="Businessman in a suit checking his phone in an office"></div>
  <div class="about-copy">
    <div class="small">Who We Are</div>
    <h2 class="display">ABOUT US</h2>
    <p>Experienced EPM resources with innovative solutions and a diverse skillset to ensure that any project can be successfully executed.</p>
    <h4>OUR MISSION</h4>
    <p>Provide clients with the highest quality EPM experience using a proven methodology that ensures client retention and satisfaction.</p>
    <a class="btn btn-blue" href="#">KNOW MORE</a>
  </div>
</section>

<section class="services">
  <div class="eyebrow">What We do</div>
  <h2 class="section-title display">OUR SERVICES</h2>
  <div class="service-row">
    <div class="service-card"><div class="service-media" role="img" aria-label="Hands working with calculator and financial papers" style="background:linear-gradient(135deg,#c8a77c,#7b6148)"></div><h3>BUDGETING AND FORECASTING</h3><p>Tarnwick specializes in both cloud and on-premises EPM solutions provided by Meridian.</p></div>
    <div class="service-card"><div class="service-media" role="img" aria-label="Team reviewing reports at a desk" style="background:linear-gradient(135deg,#d8cbb8,#8d7a62)"></div><h3>CLOSE AND CONSOLIDATION</h3><p>Tarnwick specializes in both cloud and on-premises EPM solutions provided by Meridian.</p></div>
    <div class="service-card featured"><div class="service-media" role="img" aria-label="Laptop screen showing analytics dashboards" style="background:linear-gradient(135deg,#eef2f6,#9fb4c9)"></div><h3>REPORTING AND ANALYSIS</h3><p>Traditionally, resources Planning and the Meridian EPM cloud suite provides deeper insight.</p></div>
    <div class="service-card"><div class="service-media" role="img" aria-label="Support staff with headsets at computers" style="background:linear-gradient(135deg,#d9c6b5,#6f6a66)"></div><h3>SUPPORT SERVICES</h3><p>Tarnwick offers comprehensive cross-cutting support services that provide circuit expertise.</p></div>
  </div>
</section>

<section class="why">
  <div class="eyebrow">Tarnwick Consulting</div>
  <h2 class="section-title display">WHY CHOOSE US</h2>
  <div class="why-rule"></div>
  <p class="intro">Tarnwick Consulting was founded on the principles of innovation and teamwork. We translate the products we implement through a combination of functional expertise and technical expertise. When we find limitations in the products that we implement, we see this as an opportunity and a challenge to extend those products until we meet the needs of our clients. Through this innovation we have created various tools to accelerate our implementations.</p>
  <div class="why-media" role="img" aria-label="Collage of business team photos in a tall central panel"></div>
  <div class="pillar" style="left:230px;top:380px">ACCELERATE<span class="icon-badge"><svg width="22" height="22" viewBox="0 0 24 24"><path d="M13 2L4 14h7l-1 8 9-12h-7z" fill="#fff"/></svg></span></div>
  <div class="pillar" style="left:290px;top:520px">PROCESS<span class="icon-badge"><svg width="22" height="22" viewBox="0 0 24 24"><circle cx="12" cy="12" r="7" fill="none" stroke="#fff" stroke-width="3"/><circle cx="12" cy="12" r="2" fill="#fff"/></svg></span></div>
  <div class="pillar" style="left:780px;top:380px"><span class="icon-badge"><svg width="22" height="22" viewBox="0 0 24 24"><circle cx="12" cy="10" r="6" fill="#fff"/><rect x="9" y="17" width="6" height="4" fill="#fff"/></svg></span>INNOVATIVE</div>
  <div class="pillar" style="left:780px;top:520px"><span class="icon-badge"><svg width="22" height="22" viewBox="0 0 24 24"><circle cx="8" cy="8" r="3" fill="#fff"/><circle cx="16" cy="8" r="3" fill="#fff"/><path d="M2 19a6 6 0 0112 0zM10 19a6 6 0 0112 0z" fill="#fff"/></svg></span>TEAM WORK</div>
  <div class="pillar" style="left:548px;top:670px;flex-direction:column;gap:8px"><span class="icon-badge"><svg width="22" height="22" viewBox="0 0 24 24"><path d="M4 20L20 4M14 4h6v6" fill="none" stroke="#fff" stroke-width="3"/></svg></span>STRATEGY</div>
</section>

<section class="blog">
  <div class="small">Latest Updates</div>
  <h2 class="display">OUR BLOG</h2>
  <div class="blog-arrows">
    <span style="background:#c9cdd1"><svg width="18" height="18" viewBox="0 0 24 24"><path d="M15 4l-8 8 8 8" fill="none" stroke="#fff" stroke-width="3"/></svg></span>
    <span style="background:var(--tarnwick-blue)"><svg width="18" height="18" viewBox="0 0 24 24"><path d="M9 4l8 8-8 8" fill="none" stroke="#fff" stroke-width="3"/></svg></span>
  </div>
  <div class="blog-row">
    <div class="post-card"><div class="post-media" role="img" aria-label="Folded newspaper on a desk" style="background:linear-gradient(135deg,#efefef,#a7a9ab)"></div><div class="post-date"><svg width="14" height="14" viewBox="0 0 24 24"><rect x="3" y="5" width="18" height="16" fill="#1b75bc"/></svg>October 6, 2023</div><h3>MERIDIAN CLOUD EPM UPDATES - OCTOBER ...</h3><p>Welcome back to the Tarnwick Consulting monthly Meridian Cloud EPM update.</p></div>
    <div class="post-card featured"><div class="post-media" role="img" aria-label="Award winners announcement on a dark blue background" style="background:linear-gradient(135deg,#1d2f6b,#0d1738)"></div><div class="post-date"><svg width="14" height="14" viewBox="0 0 24 24"><rect x="3" y="5" width="18" height="16" fill="#1b75bc"/></svg>October 6, 2023</div><h3>MERIDIAN CLOUD EPM UPDATES - OCTOBER ...</h3><p>Welcome back to the Tarnwick Consulting monthly Meridian Cloud EPM update.</p><a class="btn btn-blue" href="#">READ MORE</a></div>
    <div class="post-card"><div class="post-media" role="img" aria-label="Conference banner with city skyline" style="background:linear-gradient(135deg,#8fc4ea,#d96a48)"></div><div class="post-date"><svg width="14" height="14" viewBox="0 0 24 24"><rect x="3" y="5" width="18" height="16" fill="#1b75bc"/></svg>October 6, 2023</div><h3>MERIDIAN CLOUD EPM UPDATES - OCTOBER ...</h3><p>Welcome back to the Tarnwick Consulting monthly Meridian Cloud EPM update.</p></div>
  </div>
</section>

<footer class="site-footer">
  <div class="brand"><span class="brand-square"></span><span class="brand-name">TARNWICK</span></div>
  <div class="socials"><span></span><span></span></div>
  <div class="foot-col" style="left:410px"><h4>QUICK LINKS</h4><ul><li>Home</li><li>About Us</li><li>Services</li><li>Blog</li><li>Contact Us</li></ul></div>
  <div class="foot-col" style="left:590px;width:200px"><h4>CONTACT US</h4><ul><li>Call Us<br>(555) 014-2290</li><li>Mail Us<br>info@tarnwickconsulting.com</li><li>Address: Line Company Name Address</li></ul></div>
  <div class="foot-col" style="left:820px;width:280px"><h4>JOIN OUR NEWSLETTER</h4><p>Subscribe to our newsletter to get the latest news.</p><div class="subscribe"><span>Enter your email</span><b><svg width="16" height="16" viewBox="0 0 24 24"><path d="M2 12l20-9-6 19-4-8z" fill="#fff"/></svg></b></div></div>
  <div class="copyright">Copyright © 2024 All Rights Reserved by Tarnwick Consulting</div>
</footer>

</body>
</html>
```